Morvetta Designs - Online Shoe Shop

Morvetta is an online shoes and bags shop. We sell Imported Genuine Leather shoes and bags our market is LSM 8-10. We mainly sell women shoes and bags and we will also be introducing men’s shoes and belts.
I would like a website design and development that is responsive, clean, elegant and easy to use. Where customers can make a purchase online.
Have CATEGORIES in SHOE STYLE (i.e. Heels, Sandals, Pumps, Mules, Boots, Sneaker, Flats, etc) and PRICE RANGE should be in South African Rands currency, COLOUR, SIZE.
For shoe images we should be able to add videos as well.
Header and Footer Menu should have the basic menu list. Header Menu (New Arrivals, Preorder, Women’s Collection, Men’s Collection, Summer 2020 Collection, Winter 2020 Collection, Bags, Accessories, Sale, etc
Auto display when the item is SOLD OUT. Add an option for a user to get notification on when the item is back in stock.
Icons to show when shoes are on sale and Show was and now price.
Users to be able to review and rate the items.
Discount codes for new email subscribers.
Consumers should be able to pay using different options, Credit card, QuidLane, EFT, etc
Add an option for discount coupons at checkout.
After placing and order they should receive an email with order receipt.
Site should have a shipping and tracking option. International shipping such as KRT and BOLTAIR. For local shipping in South Africa please add Quickpath Couriers and Zenobi Couriers.
Backend: Backend should be easy to add more categories, items and changing header banners, adding sale alerts. To get notification when the stock is low and sold out. Get notification when an order is placed online so to prepare packing for shipping.
Can we make sure that the SEO is in place and bare in mind all searchy rules to avoid being penalized.
Target Market(s)
Women from age 25-65
LSM 8-10
Entire South Africa and neighboring countries
Industry/Entity Type
Shoe Store
Coding
Coded - Design and coding required
Number of Pages Required
5+ page
Requirements
Must have
- Responsive
Clean
Modern
Shopping cart
Shipping options integration
Newsletter subscription
Social media icons
Nice to have
- The business colors are Gold and White or Gold and Black

```html
<!DOCTYPE html>
<html lang="en">
<head>
<meta charset="utf-8">
<title>Morvetta – Product</title>
<link rel="stylesheet" href="https://fonts.googleapis.com/css2?family=Lato:wght@400;700;900&family=Montserrat:wght@500;600;700&display=swap">
<style>
:root{
  --gold:#b8924a;
  --gold-text:#c59a3e;
  --mustard:#c9a430;
  --ink:#1f1f1f;
  --text:#333;
  --muted:#666;
  --line:#cfcfcf;
  --card:#f2f2f2;
  --dark:#222;
  --darker:#151515;
  --star:#f26a1b;
}
*{box-sizing:border-box;margin:0;padding:0}
html,body{width:1200px;height:3757px;overflow:hidden}
body{position:relative;background:#fff;font-family:'Lato',sans-serif;color:var(--text)}
.abs{position:absolute}
svg.ic{display:inline-block;vertical-align:middle}

.topbar{left:0;top:0;width:1200px;height:49px;background:var(--dark);color:#fff;font-size:14px;font-weight:700;display:flex;align-items:center;justify-content:center}
.header-link{top:104px;font-size:12px;font-weight:700;color:#333;letter-spacing:.3px}
.brand{left:520px;top:68px;width:160px;text-align:center}
.brand-mark{display:block;width:44px;height:44px;margin:0 auto 6px;background:var(--ink)}
.brand-name{font-family:'Lato',sans-serif;font-weight:900;font-size:27px;color:var(--ink)}
.code-label{left:731px;top:105px;font-size:12px;font-weight:700;color:#333}
.code-badge{left:878px;top:97px;width:95px;height:31px;background:var(--gold);color:#fff;font-size:12px;font-weight:700;display:flex;align-items:center;justify-content:center}
.head-icons{left:1008px;top:103px;display:flex;gap:18px}
.cart-count{left:1108px;top:97px;width:18px;height:18px;border-radius:50%;background:var(--gold);color:#fff;font-size:11px;font-weight:700;display:flex;align-items:center;justify-content:center}
.rule{height:1px;background:var(--line)}
.nav{left:0;top:176px;width:1200px;height:56px}
.nav span{position:absolute;top:18px;font-size:16px;font-weight:700;color:#333;transform:translateX(-50%);white-space:nowrap}
.caret{display:inline-block;width:6px;height:6px;border-right:1.5px solid #333;border-bottom:1.5px solid #333;transform:rotate(45deg);margin-left:8px;position:relative;top:-3px}

.crumbs{left:74px;top:266px;font-size:12px;font-weight:700;color:#333;letter-spacing:.2px}
.crumbs b{margin:0 10px;font-weight:700}
.crumbs .here{color:var(--gold-text)}

.thumb{left:74px;width:152px;height:139px;background:var(--card)}
.thumb.active{border:2px solid var(--gold)}
.shot{position:absolute;inset:14px 18px;border-radius:6px}
.main-shot{left:240px;top:309px;width:437px;height:459px;background:var(--card)}

.p-title{left:704px;top:302px;width:420px;font-size:18px;line-height:30px;font-weight:700;color:var(--ink);letter-spacing:.2px}
.stars{display:flex;gap:4px}
.spec{left:704px;font-size:14px;color:#333}
.spec em{position:absolute;left:133px;font-style:normal;white-space:nowrap}
.select{top:612px;width:116px;height:31px;border:1px solid #bbb;font-size:13px;color:#333;padding:0 10px;display:flex;align-items:center;justify-content:space-between}
.updown{display:flex;flex-direction:column;gap:2px}
.updown i{width:0;height:0;border-left:4px solid transparent;border-right:4px solid transparent}
.updown i:first-child{border-bottom:4px solid #333}
.updown i:last-child{border-top:4px solid #333}
.price-main{left:704px;top:682px;font-size:24px;font-weight:700;color:var(--ink)}
.btn-cart{left:857px;top:672px;width:151px;height:49px;background:var(--gold);color:#fff;font-size:18px;display:flex;align-items:center;justify-content:center}
.wish{left:704px;top:743px;font-size:14px;color:#333;display:flex;align-items:center;gap:16px}

.tab{top:862px;height:36px;font-size:14px;font-weight:700;color:#222;display:flex;align-items:center}
.tab.on{left:341px;width:127px;justify-content:center;border:2px solid var(--gold);color:var(--gold-text)}
.review{left:74px;width:1052px}
.avatar{position:absolute;left:0;top:0;width:66px;height:66px;border-radius:50%;border:2px solid var(--gold);display:flex;align-items:center;justify-content:center}
.review .stars{position:absolute;left:91px;top:7px}
.review p{position:absolute;left:91px;top:28px;width:945px;font-size:15px;line-height:28px;color:#222}
.review h5{position:absolute;left:91px;top:102px;font-size:13px;font-weight:700;color:var(--gold-text);letter-spacing:.3px}

.rail-title{left:0;width:1200px;text-align:center;font-size:22px;font-weight:900;color:var(--ink)}
.card{width:246px;height:372px;background:var(--card)}
.card.raised{box-shadow:0 2px 8px rgba(0,0,0,.22)}
.card-media{position:absolute;left:40px;top:36px;width:166px;height:180px;border-radius:10px}
.card-name{position:absolute;left:14px;top:256px;font-family:'Montserrat',sans-serif;font-size:18px;font-weight:500;color:#222}
.card-price{position:absolute;left:14px;top:284px;font-family:'Montserrat',sans-serif;font-size:24px;color:var(--gold-text)}
.card-price s{font-size:18px;color:#444;margin-right:8px}
.card-meta{position:absolute;left:14px;right:14px;top:326px;font-family:Georgia,serif;font-size:12px;color:#444;display:flex;justify-content:space-between}
.card-sizes{position:absolute;left:14px;top:345px;font-size:12px;letter-spacing:5px;color:#333}
.swatches{position:absolute;right:14px;top:347px;display:flex;gap:3px}
.swatches i{width:8px;height:8px;border-radius:50%}
.flag{position:absolute;top:10px;height:30px;font-family:Georgia,serif;font-size:12px;color:#fff;display:flex;align-items:center;padding:0 12px}
.flag.in{left:-5px;background:var(--gold);clip-path:polygon(0 0,100% 0,88% 50%,100% 100%,0 100%)}
.flag.out{right:-5px;background:#111;clip-path:polygon(0 0,100% 0,100% 100%,0 100%,12% 50%)}
.quick{position:absolute;width:40px;height:40px;border-radius:50%;display:flex;align-items:center;justify-content:center}
.quick.g{background:var(--gold)}
.quick.k{background:#111}
.arrow-btn{width:50px;height:50px;border-radius:50%;background:#fff;box-shadow:0 1px 6px rgba(0,0,0,.2);display:flex;align-items:center;justify-content:center}
.arrow-btn i{width:8px;height:8px;border-left:1.5px solid #555;border-bottom:1.5px solid #555}
.arrow-btn.prev i{transform:rotate(45deg);margin-left:4px}
.arrow-btn.next i{transform:rotate(-135deg);margin-right:4px}

.promo{left:0;top:2561px;width:593px;height:539px;background:linear-gradient(135deg,#e6dccf 0%,#d8c9b6 55%,#c9b39a 100%)}
.promo-copy{left:88px;top:2612px;font-family:'Montserrat',sans-serif;color:#111}
.promo-copy h2{font-size:43px;line-height:52px;font-weight:700}
.promo-copy h2 span{color:var(--mustard)}
.promo-copy h3{margin-top:22px;font-size:22px;font-weight:500}
.promo-copy a{display:inline-block;margin-top:28px;font-size:16px;font-weight:600;color:#111;text-decoration:underline}
.newsletter{left:593px;top:2561px;width:607px;height:539px;background:var(--mustard)}
.news-copy{left:664px;top:2668px;font-family:'Montserrat',sans-serif;color:#fff;font-weight:700}
.news-copy h2{font-size:44px;line-height:50px}
.news-copy h2 small{font-size:31px}
.field{left:664px;width:448px;height:48px;background:#fff;font-family:Georgia,serif;font-size:15px;color:#777;display:flex;align-items:center;padding-left:20px}
.btn-join{left:664px;top:2932px;width:448px;height:48px;background:#000;color:#fff;font-family:'Montserrat',sans-serif;font-size:17px;font-weight:500;display:flex;align-items:center;justify-content:center}

.ship{left:0;top:3100px;width:1200px;height:271px;background:var(--dark)}
.ship-split{left:600px;top:3100px;width:1px;height:271px;background:#444}
.ship-title{top:3180px;width:600px;text-align:center;font-size:22px;font-weight:700;color:#fff;letter-spacing:.5px}
.carrier{top:3244px;font-size:30px;font-weight:900;color:#fff;white-space:nowrap}
.carrier.sm{font-size:26px}

.footer{left:0;top:3371px;width:1200px;height:386px;background:var(--darker)}
.f-head{top:3440px;font-size:14px;font-weight:700;color:#fff;letter-spacing:.3px}
.f-text{left:74px;top:3469px;font-size:14px;line-height:24px;color:#fff}
.f-text b{font-weight:400;color:var(--gold-text)}
.f-links{top:3470px;font-size:14px;line-height:32.5px;color:#ddd}
.f-brand{left:74px;top:3538px;width:92px;text-align:center}
.f-brand i{display:block;width:44px;height:44px;margin:0 auto 6px;background:#fff}
.f-brand span{font-weight:900;font-size:20px;color:#fff}
.socials{left:923px;top:3477px;display:flex;gap:10px}
.socials span{font-size:12px;font-weight:700;color:#fff}
.f-rule{left:74px;top:3653px;width:1052px;height:1px;background:#333}
.copyright{left:74px;top:3697px;font-size:12px;color:#ddd}
.pay{top:3691px;height:25px;width:43px;background:#f2f2f2;border-radius:3px;font-size:9px;font-weight:700;color:#222;display:flex;align-items:center;justify-content:center}
</style>
</head>
<body>

<svg width="0" height="0" style="position:absolute">
  <defs>
    <symbol id="star" viewBox="0 0 20 20"><path d="M10 1l2.7 5.8 6.3.7-4.7 4.3 1.3 6.2L10 14.9 4.4 18l1.3-6.2L1 7.5l6.3-.7z"/></symbol>
    <symbol id="search" viewBox="0 0 20 20"><circle cx="8.5" cy="8.5" r="6" fill="none" stroke="currentColor" stroke-width="2.6"/><path d="M13 13l5 5" stroke="currentColor" stroke-width="3" stroke-linecap="round"/></symbol>
    <symbol id="user" viewBox="0 0 20 20"><circle cx="10" cy="6" r="4.5"/><path d="M2 19c0-5 3.5-8 8-8s8 3 8 8z"/></symbol>
    <symbol id="cart" viewBox="0 0 20 20"><path d="M1 2h3l2.5 10h10l2-7H6" fill="none" stroke="currentColor" stroke-width="2.2" stroke-linejoin="round"/><path d="M5.5 5h13.5l-2 7H7.5z"/><circle cx="8" cy="16.5" r="1.8"/><circle cx="15" cy="16.5" r="1.8"/></symbol>
    <symbol id="heart" viewBox="0 0 20 20"><path d="M10 18S1 12 1 6.5A4.5 4.5 0 0 1 10 4a4.5 4.5 0 0 1 9 2.5C19 12 10 18 10 18z"/></symbol>
    <symbol id="eye" viewBox="0 0 20 20"><path d="M1 10s3.5-6 9-6 9 6 9 6-3.5 6-9 6-9-6-9-6z"/><circle cx="10" cy="10" r="3" fill="#fff"/></symbol>
    <symbol id="zoom" viewBox="0 0 20 20"><circle cx="8.5" cy="8.5" r="6" fill="none" stroke="currentColor" stroke-width="2.4"/><path d="M13 13l5 5M6 8.5h5M8.5 6v5" stroke="currentColor" stroke-width="2.4" stroke-linecap="round"/></symbol>
  </defs>
</svg>

<div class="abs topbar">Free Shipping Order Over ZAR250 within Uk</div>

<div class="abs header-link" style="left:75px">CONTACT US</div>
<div class="abs header-link" style="left:189px">TRACK ORDER</div>
<div class="abs brand"><i class="brand-mark"></i><span class="brand-name">Morvetta</span></div>
<div class="abs code-label">USE DISCOUNT CODE</div>
<div class="abs code-badge">MORVETTA50</div>
<div class="abs head-icons" style="color:#222">
  <svg class="ic" width="18" height="18"><use href="#search"/></svg>
  <svg class="ic" width="18" height="18" fill="#222"><use href="#user"/></svg>
  <svg class="ic" width="20" height="18" fill="#222"><use href="#cart"/></svg>
</div>
<div class="abs cart-count">0</div>

<div class="abs rule" style="left:0;top:175px;width:1200px"></div>
<nav class="abs nav">
  <span style="left:192px">New Arrivals</span>
  <span style="left:338px">Preorder</span>
  <span style="left:498px">2020 Collections<i class="caret"></i></span>
  <span style="left:678px">Shoes<i class="caret"></i></span>
  <span style="left:790px">Bags</span>
  <span style="left:916px">Accessories</span>
  <span style="left:1040px">Sale</span>
</nav>
<div class="abs rule" style="left:0;top:232px;width:1200px"></div>

<div class="abs crumbs">HOME<b>&gt;&gt;</b>PRODUCTS<b>&gt;&gt;</b><span class="here">PRODUCTS NAME</span></div>

<div class="abs thumb active" style="top:309px"><div class="shot" role="img" aria-label="Yellow leather handbag" style="background:linear-gradient(#f1d84a,#d9b814)"></div></div>
<div class="abs thumb" style="top:469px"><div class="shot" role="img" aria-label="Tan leather shoulder bag" style="background:linear-gradient(#c79a6e,#9b6d45)"></div></div>
<div class="abs thumb" style="top:629px"><div class="shot" role="img" aria-label="Pink structured handbag" style="background:linear-gradient(#f36e97,#de3f74)"></div></div>
<div class="abs main-shot" role="img" aria-label="Yellow leather handbag, large view">
  <div style="position:absolute;left:34px;top:110px;width:368px;height:310px;border-radius:40px 40px 16px 16px;background:linear-gradient(#f4de3e,#e5c414)"></div>
</div>

<h1 class="abs p-title">PELLENTESQUE PELLENTESQUE DIAM EGET LACUS TEMPUS MOLLIS</h1>
<div class="abs stars" style="left:704px;top:369px">
  <svg width="16" height="16" fill="var(--star)"><use href="#star"/></svg><svg width="16" height="16" fill="var(--star)"><use href="#star"/></svg><svg width="16" height="16" fill="var(--star)"><use href="#star"/></svg><svg width="16" height="16" fill="var(--star)"><use href="#star"/></svg><svg width="16" height="16" fill="var(--star)"><use href="#star"/></svg>
</div>
<div class="abs spec" style="top:403px">Availability:<em>Available</em></div>
<div class="abs spec" style="top:436px">SKU:<em>327AE-6</em></div>
<div class="abs spec" style="top:469px">Barcode:<em>327038522</em></div>
<div class="abs spec" style="top:502px">Collections:<em>Bag, Women's</em></div>
<div class="abs spec" style="top:535px">Product type:<em>Stridewell Pro</em></div>
<div class="abs spec" style="top:568px">Vendor:<em>Lumawear</em></div>
<div class="abs select" style="left:704px">Size<span class="updown"><i></i><i></i></span></div>
<div class="abs select" style="left:832px">Color<span class="updown"><i></i><i></i></span></div>
<div class="abs select" style="left:959px">Qty<span class="updown"><i></i><i></i></span></div>
<div class="abs price-main">ZAR55.00</div>
<div class="abs btn-cart">Add to Cart</div>
<div class="abs wish"><svg width="15" height="14" fill="#222"><use href="#heart"/></svg>Add to the wishlist</div>

<div class="abs rule" style="left:74px;top:829px;width:1052px;background:#bbb"></div>
<div class="abs tab" style="left:87px">DESCRIPTION</div>
<div class="abs tab" style="left:243px">DELIVERY</div>
<div class="abs tab on">REVIEWS</div>

<div class="abs review" style="top:945px">
  <div class="avatar"><svg width="24" height="24" fill="#444"><use href="#user"/></svg></div>
  <div class="stars"><svg width="14" height="14" fill="var(--gold)"><use href="#star"/></svg><svg width="14" height="14" fill="var(--gold)"><use href="#star"/></svg><svg width="14" height="14" fill="var(--gold)"><use href="#star"/></svg><svg width="14" height="14" fill="var(--gold)"><use href="#star"/></svg><svg width="14" height="14" fill="var(--gold)"><use href="#star"/></svg></div>
  <p>“ Curabitur ac gravida ipsum ellentesque pellentesque diam eget lacus tempus mollis et mollis leo mauris sed erat elem entum finibus<br>quis eleifend nunc eros commodo risus..”</p>
  <h5>NAME HEADING</h5>
</div>
<div class="abs rule" style="left:74px;top:1076px;width:1052px;background:#bbb"></div>
<div class="abs review" style="top:1095px">
  <div class="avatar"><svg width="24" height="24" fill="#444"><use href="#user"/></svg></div>
  <div class="stars"><svg width="14" height="14" fill="var(--gold)"><use href="#star"/></svg><svg width="14" height="14" fill="var(--gold)"><use href="#star"/></svg><svg width="14" height="14" fill="var(--gold)"><use href="#star"/></svg><svg width="14" height="14" fill="var(--gold)"><use href="#star"/></svg><svg width="14" height="14" fill="var(--gold)"><use href="#star"/></svg></div>
  <p>“ Curabitur ac gravida ipsum ellentesque pellentesque diam eget lacus tempus mollis et mollis leo mauris sed erat elem entum finibus<br>quis eleifend nunc eros commodo risus..”</p>
  <h5>NAME HEADING</h5>
</div>
<div class="abs rule" style="left:74px;top:1226px;width:1052px;background:#bbb"></div>
<div class="abs review" style="top:1241px">
  <div class="avatar"><svg width="24" height="24" fill="#444"><use href="#user"/></svg></div>
  <div class="stars"><svg width="14" height="14" fill="var(--gold)"><use href="#star"/></svg><svg width="14" height="14" fill="var(--gold)"><use href="#star"/></svg><svg width="14" height="14" fill="var(--gold)"><use href="#star"/></svg><svg width="14" height="14" fill="var(--gold)"><use href="#star"/></svg><svg width="14" height="14" fill="var(--gold)"><use href="#star"/></svg></div>
  <p>“ Curabitur ac gravida ipsum ellentesque pellentesque diam eget lacus tempus mollis et mollis leo mauris sed erat elem entum finibus<br>quis eleifend nunc eros commodo risus..”</p>
  <h5>NAME HEADING</h5>
</div>
<div class="abs rule" style="left:74px;top:1397px;width:1052px;background:#bbb"></div>

<h2 class="abs rail-title" style="top:1448px">YOU MAY ALSO LIKE</h2>

<div class="abs card" style="left:79px;top:1520px">
  <div class="card-media" role="img" aria-label="Yellow dome handbag" style="background:linear-gradient(#f4cf3a,#e6b51a)"></div>
  <div class="card-name">Product Name</div><div class="card-price"><s>R150</s>R100</div>
  <div class="card-meta"><span>Select Size</span><span>Choose Color</span></div><div class="card-sizes">S M L</div>
  <div class="swatches"><i style="background:#c9a430"></i><i style="background:#111"></i><i style="background:#e01b1b"></i><i style="background:#f05a1a"></i></div>
</div>
<div class="abs card raised" style="left:346px;top:1520px">
  <div class="card-media" role="img" aria-label="Gold metallic evening bag" style="background:linear-gradient(#e6c98a,#b8904a)"></div>
  <div class="card-name">Product Name</div><div class="card-price"><s>R150</s>R100</div>
  <div class="card-meta"><span>Select Size</span><span>Choose Color</span></div><div class="card-sizes">S M L</div>
  <div class="swatches"><i style="background:#c9a430"></i><i style="background:#111"></i><i style="background:#e01b1b"></i><i style="background:#f05a1a"></i></div>
</div>
<div class="abs card" style="left:615px;top:1520px">
  <div class="card-media" role="img" aria-label="Brown leather ankle boots" style="background:linear-gradient(#7a6050,#4a3628)"></div>
  <div class="card-name">Product Name</div><div class="card-price"><s>R150</s>R100</div>
  <div class="card-meta"><span>Select Size</span><span>Choose Color</span></div><div class="card-sizes">S M L</div>
  <div class="swatches"><i style="background:#c9a430"></i><i style="background:#111"></i><i style="background:#e01b1b"></i><i style="background:#f05a1a"></i></div>
</div>
<div class="abs card" style="left:884px;top:1520px">
  <div class="card-media" role="img" aria-label="Brown leather belt" style="background:linear-gradient(#a8582e,#76381a)"></div>
  <div class="card-name">Product Name</div><div class="card-price"><s>R150</s>R100</div>
  <div class="card-meta"><span>Select Size</span><span>Choose Color</span></div><div class="card-sizes">S M L</div>
  <div class="swatches"><i style="background:#c9a430"></i><i style="background:#111"></i><i style="background:#e01b1b"></i><i style="background:#f05a1a"></i></div>
</div>
<div class="abs arrow-btn prev" style="left:50px;top:1681px"><i></i></div>
<div class="abs arrow-btn next" style="left:1098px;top:1681px"><i></i></div>

<div class="abs rule" style="left:74px;top:1974px;width:1052px;background:#bbb"></div>

<h2 class="abs rail-title" style="top:2040px">RECENTLY VIEWED</h2>

<div class="abs card" style="left:79px;top:2112px">
  <span class="flag in">In stock</span>
  <div class="card-media" role="img" aria-label="Red patent stiletto pumps" style="background:linear-gradient(#e32a2a,#a80f12)"></div>
  <div class="card-name">Product Name</div><div class="card-price"><s>R150</s>R100</div>
  <div class="card-meta"><span>Select Size</span><span>Choose Color</span></div><div class="card-sizes">S M L</div>
  <div class="swatches"><i style="background:#c9a430"></i><i style="background:#111"></i><i style="background:#e01b1b"></i><i style="background:#f05a1a"></i></div>
</div>
<div class="abs card raised" style="left:346px;top:2112px">
  <span class="flag in">In stock</span>
  <div class="card-media" role="img" aria-label="Pink leather tote bag" style="background:linear-gradient(#f28aa0,#e05474)"></div>
  <div class="quick g" style="left:68px;top:104px"><svg width="18" height="18" fill="#fff"><use href="#eye"/></svg></div>
  <div class="quick k" style="left:130px;top:104px"><svg width="18" height="18" fill="#fff"><use href="#cart"/></svg></div>
  <div class="quick k" style="left:68px;top:162px"><svg width="18" height="18" fill="#fff"><use href="#heart"/></svg></div>
  <div class="quick g" style="left:130px;top:162px;color:#fff"><svg width="18" height="18"><use href="#zoom"/></svg></div>
  <div class="card-name">Product Name</div><div class="card-price"><s>R150</s>R100</div>
  <div class="card-meta"><span>Select Size</span><span>Choose Color</span></div><div class="card-sizes">S M L</div>
  <div class="swatches"><i style="background:#c9a430"></i><i style="background:#111"></i><i style="background:#e01b1b"></i><i style="background:#f05a1a"></i></div>
</div>
<div class="abs card" style="left:615px;top:2112px">
  <span class="flag out">Sold Out</span>
  <div class="card-media" role="img" aria-label="Blue running sneakers" style="background:linear-gradient(#2f4fd0,#1a2e90)"></div>
  <div class="card-name">Product Name</div><div class="card-price"><s>R150</s>R100</div>
  <div class="card-meta"><span>Select Size</span><span>Choose Color</span></div><div class="card-sizes">S M L</div>
  <div class="swatches"><i style="background:#c9a430"></i><i style="background:#111"></i><i style="background:#e01b1b"></i><i style="background:#f05a1a"></i></div>
</div>
<div class="abs card" style="left:884px;top:2112px">
  <div class="card-media" role="img" aria-label="Cognac leather satchel" style="background:linear-gradient(#a5512d,#6e2f16)"></div>
  <div class="card-name">Product Name</div><div class="card-price"><s>R150</s>R100</div>
  <div class="card-meta"><span>Select Size</span><span>Choose Color</span></div><div class="card-sizes">S M L</div>
  <div class="swatches"><i style="background:#c9a430"></i><i style="background:#111"></i><i style="background:#e01b1b"></i><i style="background:#f05a1a"></i></div>
</div>
<div class="abs arrow-btn prev" style="left:50px;top:2273px"><i></i></div>
<div class="abs arrow-btn next" style="left:1098px;top:2273px"><i></i></div>

<div class="abs promo" role="img" aria-label="Legs in black leggings wearing black suede stiletto heels on a warm beige backdrop"></div>
<div class="abs promo-copy">
  <h2>Get <span>75%</span><br>Offer</h2>
  <h3>Women Footwear</h3>
  <a>Buy Now</a>
</div>
<div class="abs newsletter"></div>
<div class="abs news-copy"><h2>Join Our Newsletter<br>For <small>Get Discount codes</small></h2></div>
<div class="abs field" style="top:2810px">User Name</div>
<div class="abs field" style="top:2871px">Email ID</div>
<div class="abs btn-join">Join Now</div>

<div class="abs ship"></div>
<div class="abs ship-split"></div>
<div class="abs ship-title" style="left:30px">INTERNATIONAL SHIPPING</div>
<div class="abs ship-title" style="left:570px">LOCAL SHIPPING</div>
<div class="abs carrier" style="left:130px">KRT</div>
<div class="abs carrier" style="left:364px">BOLTAIR</div>
<div class="abs carrier sm" style="left:684px;top:3230px">Quickpath<br><span style="font-size:15px;font-weight:400">Couriers</span></div>
<div class="abs carrier sm" style="left:893px;top:3230px">Zenobi<br><span style="font-size:15px;font-weight:400">Couriers</span></div>

<footer class="abs footer"></footer>
<div class="abs f-head" style="left:74px">CONTACT US</div>
<div class="abs f-text">Any questions? Let us know in store at<br>48 Harbour Lane, or call us on <b>1800 555 014.</b></div>
<div class="abs f-brand"><i></i><span>Morvetta</span></div>
<div class="abs f-head" style="left:461px">QUICK LINKS</div>
<div class="abs f-links" style="left:461px">New Arrivals<br>Preorder<br>Women's Collection<br>Men's Collection<br>Summer 2020 Collection</div>
<div class="abs f-links" style="left:677px">Winter 2020 Collection<br>Bags<br>Accessories<br>Sale</div>
<div class="abs f-head" style="left:923px">SOCIAL NETWORKS</div>
<div class="abs socials"><span>Facenet</span><span>Chirper</span><span>Snapgram</span><span>Pinboard</span></div>
<div class="abs f-rule"></div>
<div class="abs copyright">Copyright © 2020. Company Name. All Right Reserved</div>
<div class="abs pay" style="left:792px">Tollen</div>
<div class="abs pay" style="left:850px">Pennio</div>
<div class="abs pay" style="left:908px">Brisca</div>
<div class="abs pay" style="left:966px">QuidLane</div>
<div class="abs pay" style="left:1024px">Ormand</div>
<div class="abs pay" style="left:1083px">Kelvo</div>

</body>
</html>
```